Guarding One's Body Using Sharp Steel Cover

Hi we are producing a self defense course entitled Guarding One's Body Using Sharp Steel: A Complete Manual For Learning The Finest And Handiest Wilderness Tool In Recorded History.

I listed this as a book cover but it will actually be a DVD set, but the book cover model works fine.

See below for design examples - I am thinking we need a cover that will appeal to military/survival type people.

Target Market(s)

survivalists, cops, preppers, gun owners, martial artists, and average people wanting to learn how to defend themselves

Industry/Entity Type

Defense

Requirements
Must have
• Title: GUARDING ONE'S BODY USING SHARP STEEL: A COMPLETE MANUAL FOR LEARNING THE FINEST AND HANDIEST WILDERNESS TOOL IN RECORDED HISTORY
Nice to have
• Please look at these sample designs from other books as a model:
• https://files.plorvexa.org/media/en/4/27/BrindelQXMP.jpg - This stye is ideal.
• Other good examples:
• https://pics2.talvorn.com/8143907_k370.jpg
• http://m.zephquill.com/titles/2719058463k/48071935.jpg
• http://img.crondelmart.com/pics/P/73Tm58QyzFr._BX_KL410_TR316,410_.jpg
• http://3.cdn.wendoplix.net/-RTyZWLMMKAQ/BNWq_hufxaT/BBBBBBBBv8G/DKNp815ZaXW/s1600/Q4710392.JPG

```html
<!DOCTYPE html>
<html lang="en">
<head>
<meta charset="utf-8">
<title>Guarding One's Body Using Sharp Steel – Cover</title>
<link href="https://fonts.googleapis.com/css2?family=Ultra&family=Montserrat:wght@800;900&display=swap" rel="stylesheet">
<style>
  :root {
    --cover-orange: #d9874a;
    --cover-light: #e4a064;
    --cover-burnt: #cf6a2c;
    --ink: #141210;
    --shadow-line: #f0c08e;
    --blade-tone: #8a5a3c;
    --handle-tone: #6e4530;
  }
  * { margin: 0; padding: 0; box-sizing: border-box; }
  html, body { width: 970px; height: 1200px; overflow: hidden; }
  body { background: var(--cover-orange); }

  .cover {
    position: relative;
    width: 970px;
    height: 1200px;
    overflow: hidden;
    background:
      radial-gradient(ellipse 60% 30% at 50% 42%, rgba(207,90,30,0.55), rgba(207,90,30,0) 100%),
      radial-gradient(ellipse 90% 70% at 50% 50%, var(--cover-light) 0%, var(--cover-orange) 70%, #c9773e 100%);
    color: var(--ink);
  }

  .title {
    position: absolute;
    left: 0; right: 0; top: 70px;
    text-align: center;
    font-family: "Ultra", Georgia, serif;
    line-height: 1;
    text-transform: uppercase;
  }
  .title-line {
    display: block;
    text-shadow: 4px 5px 0 var(--shadow-line), 6px 7px 0 var(--ink);
  }
  .title-line--top { font-size: 70px; letter-spacing: 1px; }
  .title-line--mid { font-size: 104px; letter-spacing: 1px; margin-top: 14px; }
  .title-line--low { font-size: 86px; letter-spacing: 2px; margin-top: 16px; }

  .knife-art {
    position: absolute;
    left: 130px; top: 470px;
    width: 720px; height: 150px;
  }

  .subtitle {
    position: absolute;
    left: 155px; width: 680px; top: 700px;
    font-family: "Montserrat", Arial, sans-serif;
    font-weight: 900;
    text-transform: uppercase;
    line-height: 1.05;
  }
  .subtitle-line { display: block; white-space: nowrap; }
  .subtitle-line--1 { font-size: 50px; letter-spacing: 2px; }
  .subtitle-line--2 { font-size: 40px; letter-spacing: 1px; }
  .subtitle-line--3 { font-size: 36px; letter-spacing: 0; }
  .subtitle-line--4 { font-size: 52px; letter-spacing: 3px; }
  .subtitle-line--5 { font-size: 78px; letter-spacing: 6px; }

  .author {
    position: absolute;
    left: 0; right: 0; top: 1060px;
    text-align: center;
    font-family: "Ultra", Georgia, serif;
    font-size: 74px;
    letter-spacing: 2px;
    text-transform: uppercase;
    text-shadow: 4px 5px 0 var(--shadow-line), 6px 7px 0 var(--ink);
  }
</style>
</head>
<body>
  <main class="cover">
    <h1 class="title">
      <span class="title-line title-line--top">Guarding One's</span>
      <span class="title-line title-line--mid">Body Using</span>
      <span class="title-line title-line--low">Sharp Steel</span>
    </h1>

    <svg class="knife-art" viewBox="0 0 720 150" role="img" aria-label="Engraved illustration of a combat survival knife with ridged handle and serrated blade">
      <defs>
        <linearGradient id="knifeTone" x1="0" x2="1" y1="0" y2="0">
          <stop offset="0" stop-color="var(--handle-tone)"/>
          <stop offset="0.4" stop-color="var(--handle-tone)"/>
          <stop offset="1" stop-color="var(--blade-tone)"/>
        </linearGradient>
      </defs>
      <rect x="0" y="0" width="720" height="150" rx="10" fill="url(#knifeTone)" opacity="0.55"/>
    </svg>

    <h2 class="subtitle">
      <span class="subtitle-line subtitle-line--1">A Complete Manual</span>
      <span class="subtitle-line subtitle-line--2">For Learning The Finest</span>
      <span class="subtitle-line subtitle-line--3">And Handiest Wilderness</span>
      <span class="subtitle-line subtitle-line--4">Tool In Recorded</span>
      <span class="subtitle-line subtitle-line--5">History</span>
    </h2>

    <p class="author">Author Name</p>
  </main>
</body>
</html>
```